Oregon Pawnbroker About Us Brochure

We need to make a front/back tri-fold "about us" informative brochure using the bullet points uploaded. Our association represents licensed pawnbrokers in the state of Oregon and this will be distributed to the entire legislative body in our state. I have attached our logo, but feel free to be creative with logo to enhance the overall appearance of the brochure.

Target Market(s)

Regulators and Politicians

Industry/Entity Type

Pawnbroker

Requirements
Must have
• Professional Appearance
Nice to have
• Graphics, color scheme

```html
<!DOCTYPE html>
<html lang="en">
<head>
<meta charset="utf-8">
<title>Pacific Pawn Lenders Alliance – Tri-fold Brochure</title>
<link rel="stylesheet" href="https://fonts.googleapis.com/css2?family=Oswald:wght@300;400&family=Poppins:wght@300;400&display=swap">
<style>
:root{
  --stage:#6b6c6e;
  --paper:#ffffff;
  --paper-tint:#eeeeef;
  --slate:#a7a9ac;
  --slate-dark:#939598;
  --orange:#f07a1e;
  --ink:#2b2b2b;
  --ink-soft:#6a6a6a;
  --rule:#d4d4d4;
}
*{margin:0;padding:0;box-sizing:border-box}
html,body{width:755px;height:1200px;overflow:hidden;background:var(--stage)}
body{position:relative;font-family:"Poppins",Arial,sans-serif;color:var(--ink)}
.sheet{position:absolute;left:56px;width:654px;height:508px;background:var(--paper);box-shadow:0 8px 14px rgba(0,0,0,.35);overflow:hidden}
.sheet--outside{top:61px}
.sheet--inside{top:628px}
.panel{position:absolute;top:0;height:508px}
.p1{left:0;width:213px}
.p2{left:213px;width:216px}
.p3{left:429px;width:225px}
.tint{background:linear-gradient(90deg,#fff 0%,#f7f7f7 60%,#e6e6e7 100%)}
.slate{background:linear-gradient(90deg,#b0b2b5,#9d9fa2)}
.heading{font-family:"Oswald",Arial Narrow,sans-serif;font-weight:300;text-transform:uppercase;line-height:1.3;letter-spacing:-.2px}
.heading--orange{color:var(--orange);font-size:14px}
.heading--dark{color:var(--ink);font-size:15px}
.heading--light{color:#fff;font-size:14px}
.rule{position:absolute;height:2px;background:var(--orange)}
.body-text{font-size:7.4px;line-height:1.45}
.small{font-size:6.4px;line-height:1.45;color:var(--ink-soft)}
.abs{position:absolute}
.feature{position:absolute;left:20px;width:238px;display:flex;gap:6px;align-items:flex-start}
.feature .icon{flex:0 0 20px;height:20px}
.feature p{width:155px;text-align:justify}
.sep{position:absolute;left:20px;width:177px;border-top:1px dotted var(--rule)}
.photo{position:absolute}
.web-bar{position:absolute;bottom:8px;height:21px;background:var(--orange);color:#fff;font-size:6.8px;display:flex;align-items:center;justify-content:center}
.seal{position:absolute;border-radius:50%;background:#fff;border:2px solid #d7d7d7;display:flex;align-items:center;justify-content:center;text-align:center}
.seal span{font-family:"Oswald",Arial Narrow,sans-serif;font-weight:400;font-size:10px;line-height:1.2;color:var(--ink);text-transform:uppercase}
.center{text-align:center}
.white{color:#fff}
.bullets li{list-style:none;position:relative;padding-left:11px;margin-bottom:7px}
.bullets li::before{content:"";position:absolute;left:0;top:1px;width:6px;height:6px;border-radius:50%;background:var(--orange)}
.sublist li{list-style:none;margin:0 0 3px 0}
.ticks li{list-style:none;display:flex;align-items:center;gap:5px;font-size:6.6px;color:#fff;margin-bottom:6px}
.pill{position:absolute;height:15px;border-radius:8px;background:var(--orange);color:#fff;font-size:6.5px;display:flex;align-items:center;justify-content:center}
</style>
</head>
<body>

<!-- OUTSIDE -->
<section class="sheet sheet--outside">
  <div class="panel p1 tint">
    <h2 class="heading heading--orange abs" style="left:22px;top:30px;width:180px">Why pawnbrokers are important to Oregon consumers</h2>
    <div class="rule" style="left:22px;top:68px;width:55px"></div>
    <p class="body-text abs" style="left:22px;top:82px;width:178px;text-align:justify">Without state-licensed pawnbrokers, Oregonians could be forced to borrow from unlicensed people with unregulated loans that include very high interest rates or instead, forced to sell their property entirely, diminishing their personal assets.</p>
    <div class="sep" style="top:160px"></div>
    <div class="feature" style="top:166px">
      <svg class="icon" viewBox="0 0 20 20" fill="none" stroke="var(--orange)" stroke-width="1.2"><rect x="2" y="5" width="16" height="10" rx="1"/><circle cx="10" cy="10" r="2.5"/></svg>
      <p class="small">Other credit based lenders, such as banks and credit unions, do not offer Oregonians loan products at the small dollar amounts our industry serves.</p>
    </div>
    <div class="sep" style="top:204px"></div>
    <div class="feature" style="top:212px">
      <svg class="icon" viewBox="0 0 20 20" fill="none" stroke="var(--orange)" stroke-width="1.2"><circle cx="10" cy="10" r="7"/><path d="M10 5v5l3 2"/></svg>
      <p class="small">Pawnbrokers provide a same day financial solution.</p>
    </div>
    <div class="sep" style="top:242px"></div>
    <div class="feature" style="top:250px">
      <svg class="icon" viewBox="0 0 20 20" fill="none" stroke="var(--orange)" stroke-width="1.2"><circle cx="10" cy="10" r="7"/><circle cx="10" cy="8" r="2"/><path d="M6 14c1-2 7-2 8 0"/></svg>
      <p class="small">Pawnbrokers are invested in our communities and are sensitive to the needs of our customers.</p>
    </div>
    <div class="sep" style="top:284px"></div>
    <svg class="photo" style="left:0;top:330px" width="213" height="178" viewBox="0 0 213 178" role="img" aria-label="Photo of colleagues shaking hands in a bright office">
      <defs><linearGradient id="g1" x1="0" y1="0" x2="1" y2="1"><stop offset="0" stop-color="#c9cdd2"/><stop offset=".5" stop-color="#8a8f96"/><stop offset="1" stop-color="#4e5258"/></linearGradient></defs>
      <path d="M0 10 Q110 -12 213 60 V178 H0Z" fill="url(#g1)"/>
      <path d="M120 4 Q180 20 213 52" fill="none" stroke="#cfcfd1" stroke-width="6"/>
    </svg>
  </div>

  <div class="panel p2 slate">
    <div class="seal" style="left:50px;top:62px;width:116px;height:116px"><span>Pacific Pawn<br>Lenders<br>Alliance</span></div>
    <p class="abs center white" style="left:20px;top:210px;width:176px;font-size:7px;line-height:1.4">Our association represents licensed pawnbrokers in the state of Oregon and this will be distributed to the entire legislative body in our state.</p>
    <div class="rule" style="left:80px;top:276px;width:56px"></div>
    <p class="abs center white heading" style="left:20px;top:298px;width:176px;font-size:9.5px;line-height:1.55">Not a member?<br>Interested in becoming a one?<br>What are you waiting for?<br>Join PPLA today.</p>
    <div class="rule" style="left:80px;top:372px;width:56px"></div>
    <p class="abs center white" style="left:10px;top:397px;width:196px;font-size:6.6px;line-height:1.7">Maple Street Pawn &amp; Loan<br>c/o Pacific Pawn Lenders Alliance<br>4210 NW Harbor Ave Ste B<br>Salem, OR 97301</p>
    <div class="web-bar" style="left:0;width:216px;bottom:9px">www.pacificpawnlenders.org</div>
  </div>

  <div class="panel p3" style="background:linear-gradient(180deg,#fff 60%,#ececed)">
    <svg class="photo" style="left:0;top:0" width="225" height="330" viewBox="0 0 225 330" role="img" aria-label="Photo of smiling professionals gathered around a meeting table">
      <defs><linearGradient id="g2" x1="0" y1="0" x2="1" y2="1"><stop offset="0" stop-color="#b8a596"/><stop offset=".45" stop-color="#7d7f8a"/><stop offset="1" stop-color="#dfe1e4"/></linearGradient></defs>
      <path d="M0 0 H225 V262 Q130 290 0 322Z" fill="url(#g2)"/>
      <path d="M20 322 Q120 288 225 266" fill="none" stroke="#c9c9cb" stroke-width="5"/>
    </svg>
    <div class="seal" style="left:56px;top:284px;width:114px;height:114px"><span>Pacific Pawn<br>Lenders<br>Alliance</span></div>
    <h2 class="heading heading--dark abs center" style="left:10px;top:428px;width:205px;font-size:15px">Quick facts about<br>Oregon pawnbrokers</h2>
    <div class="web-bar" style="left:0;width:225px;bottom:9px">www.pacificpawnlenders.org</div>
  </div>
</section>

<!-- INSIDE -->
<section class="sheet sheet--inside">
  <div class="panel p1 tint">
    <h2 class="heading heading--orange abs" style="left:22px;top:27px">About our industry</h2>
    <div class="rule" style="left:22px;top:51px;width:55px"></div>
    <p class="body-text abs" style="left:22px;top:58px;width:180px">Pawnbroking is the oldest form of regulated consumer credit.</p>
    <div class="feature" style="top:84px">
      <svg class="icon" viewBox="0 0 20 20" fill="none" stroke="var(--orange)" stroke-width="1.2"><rect x="4" y="2" width="12" height="16" rx="1"/><path d="M7 7h6M7 10h6M7 13h4"/></svg>
      <p class="small">The Department of Consumer and Business Services issues the pawnbroker licenses here in Oregon.</p>
    </div>
    <div class="feature" style="top:123px">
      <svg class="icon" viewBox="0 0 20 20" fill="none" stroke="var(--orange)" stroke-width="1.2"><rect x="2" y="3" width="16" height="14" rx="1"/><path d="M5 14l4-4 3 2 4-5"/></svg>
      <p class="small">Currently, Oregon has 83 individually licensed pawnshops, 78 of which are brick-and-mortar, family-owned and operated businesses.</p>
    </div>
    <div class="feature" style="top:162px">
      <svg class="icon" viewBox="0 0 20 20" fill="none" stroke="var(--orange)" stroke-width="1.2"><circle cx="10" cy="8" r="5"/><path d="M4 18c1-3 11-3 12 0"/></svg>
      <p class="small">Pawnbrokers offer highly regulated safety-net funds to consumers on a face-to-face basis from Main Street locations across the state.</p>
    </div>
    <div class="feature" style="top:210px">
      <svg class="icon" viewBox="0 0 20 20" fill="none" stroke="var(--orange)" stroke-width="1.2"><circle cx="10" cy="10" r="7"/><path d="M12 7h-3a1.5 1.5 0 000 3h2a1.5 1.5 0 010 3H8M10 5v10"/></svg>
      <p class="small">Lending decisions are solely based on the collateral and pawn transactions are non-recourse. No credit inquiries, No credit reporting, No collections, No cycle of debt.</p>
    </div>
    <div class="feature" style="top:260px">
      <svg class="icon" viewBox="0 0 20 20" fill="none" stroke="var(--orange)" stroke-width="1.2"><rect x="3" y="3" width="14" height="14" rx="2"/><path d="M7 10l2 2 4-4"/></svg>
      <p class="small">Pawnbrokers provide safe, secure storage for items customers cannot or do not want to store themselves, including oversized or seasonal items construction equipment, and firearms.</p>
    </div>
    <svg class="photo" style="left:0;top:312px" width="213" height="196" viewBox="0 0 213 196" role="img" aria-label="Photo of two smiling women reviewing documents together, with an inset photo of teammates stacking hands">
      <defs>
        <linearGradient id="g3" x1="0" y1="0" x2="1" y2="1"><stop offset="0" stop-color="#5e6d7c"/><stop offset=".5" stop-color="#a49382"/><stop offset="1" stop-color="#3f4650"/></linearGradient>
        <radialGradient id="g4"><stop offset="0" stop-color="#c8a68c"/><stop offset="1" stop-color="#7c8a99"/></radialGradient>
      </defs>
      <path d="M0 26 Q100 0 213 24 V196 H0Z" fill="url(#g3)"/>
      <path d="M0 20 Q80 0 140 8" fill="none" stroke="#d0d0d2" stroke-width="5"/>
      <circle cx="177" cy="45" r="47" fill="#fff"/>
      <circle cx="177" cy="45" r="43" fill="url(#g4)"/>
    </svg>
  </div>

  <div class="panel p2 tint" style="left:218px;width:211px">
    <h2 class="heading heading--orange abs center" style="left:0;top:40px;width:211px">Regulation</h2>
    <p class="body-text abs center" style="left:12px;top:66px;width:187px">Pawnshops are heavily regulated and work closely with the federal, state and local governments and law enforcement.</p>
    <div class="rule" style="left:78px;top:114px;width:56px"></div>
    <ul class="bullets small abs" style="left:8px;top:139px;width:196px">
      <li>ORS 726 and OAR 441-740 define the requirements for our industry here in Oregon including the requirements of a loan, duration of a loan, as well as the interest and fees charged.</li>
      <li>Transactions require customer to present government issued photo identification.</li>
      <li>All transactions are reported daily to law enforcement.</li>
      <li>Oregon Pawnbrokers work closely with the following regulators:</li>
    </ul>
    <ul class="sublist small abs" style="left:19px;top:264px;width:185px">
      <li>• Department of Consumer and Business Services</li>
      <li>• Bureau of Alcohol Tobacco and Firearms</li>
      <li>• State Police</li>
      <li>• Department of Agriculture</li>
    </ul>
  </div>

  <div class="panel p3" style="background:linear-gradient(180deg,#fff,#f3f3f4)">
    <svg class="photo" style="left:0;top:0" width="225" height="200" viewBox="0 0 225 200" role="img" aria-label="Photo of a team talking around a table in a brick-walled office">
      <defs><linearGradient id="g5" x1="0" y1="0" x2="1" y2="1"><stop offset="0" stop-color="#9c6b52"/><stop offset=".5" stop-color="#c9b7a6"/><stop offset="1" stop-color="#4d5660"/></linearGradient></defs>
      <circle cx="118" cy="70" r="116" fill="none" stroke="#c9c9cb" stroke-width="5"/>
      <circle cx="118" cy="70" r="110" fill="url(#g5)"/>
    </svg>
    <h3 class="heading abs" style="left:18px;top:206px;font-size:12px;color:var(--ink)">Oregon pawnbroker statistics</h3>
    <p class="small abs" style="left:18px;top:223px;color:var(--ink)">(as reported by DCBS)</p>
    <div class="rule" style="left:18px;top:236px;width:56px"></div>
    <div class="abs small" style="left:18px;top:248px;width:200px;color:var(--ink)">
      <p style="margin-bottom:3px">Average loan amount in 2020 was $175</p>
      <p style="margin-bottom:9px">• Redemption rate of 72%</p>
      <p style="margin-bottom:6px">• Oregon pawnshops made approximately 206,500 loans in 2020, lending $33.2 million to Oregon customers.</p>
      <p>• Police pickup rate of 0.085%</p>
    </div>
  </div>

  <div class="abs slate" style="left:218px;top:345px;width:436px;height:155px"></div>
  <h2 class="heading heading--light abs" style="left:242px;top:364px;font-size:13.5px">About the Pacific Pawn<br>Lenders Alliance</h2>
  <div class="abs white" style="left:242px;top:406px;width:180px;font-size:6.5px;line-height:1.45">
    <p style="margin-bottom:9px">United voice of Oregon Pawnbrokers</p>
    <p style="margin-bottom:9px">• Represents majority of pawnbrokers, both number of licensees and transactions processed</p>
    <p>• Single point of contact for Oregon Legislature and all regulators to communicate with our industry.</p>
  </div>
  <h2 class="heading heading--light abs center" style="left:429px;top:364px;width:225px;font-size:13.5px">Quick facts about<br>Oregon pawnbrokers</h2>
  <ul class="ticks abs" style="left:483px;top:408px">
    <li><svg width="9" height="9" viewBox="0 0 9 9"><rect width="9" height="9" rx="2" fill="var(--orange)"/><path d="M2 4.5l1.8 1.8L7 3" stroke="#fff" stroke-width="1.2" fill="none"/></svg>NO CREDIT INQUIRIES</li>
    <li><svg width="9" height="9" viewBox="0 0 9 9"><rect width="9" height="9" rx="2" fill="var(--orange)"/><path d="M2 4.5l1.8 1.8L7 3" stroke="#fff" stroke-width="1.2" fill="none"/></svg>NO CREDIT REPORTING</li>
    <li><svg width="9" height="9" viewBox="0 0 9 9"><rect width="9" height="9" rx="2" fill="var(--orange)"/><path d="M2 4.5l1.8 1.8L7 3" stroke="#fff" stroke-width="1.2" fill="none"/></svg>NO COLLECTIONS</li>
    <li><svg width="9" height="9" viewBox="0 0 9 9"><rect width="9" height="9" rx="2" fill="var(--orange)"/><path d="M2 4.5l1.8 1.8L7 3" stroke="#fff" stroke-width="1.2" fill="none"/></svg>NO CYCLE OF DEBT</li>
  </ul>
  <div class="pill" style="left:471px;top:480px;width:141px">www.pacificpawnlenders.org</div>
</section>

</body>
</html>
```